Thornvale Secure Business Cards

Need high quality business card designed around my company logo. Ideally the cards need to be a glossy black as the logo goes well with a black background.

The company is a Locksmithing business.

Domestic clients are Residential Home Owners and Landlords. Commercial clients are local businesses, estate agents, landlords, solicitors

Services offered :
Emergency Lock Out
New Lock Fitting & Replacement
High Security Upgrades
UPVC lock repairs
Mobile Key Cutting
Free Security Reviews

Qualificatons & Certifications:
Accredited Fenwick & Marrow NVQ Level 3, TQBA
Fully Insured
PVR Checked

Contact & Business Details:

Business Name : Thornvale Secure
Name: Rob Kessington
Tel: 01632 960481 Office / 07700900417 Mobile
Email: contact@thornvalesecure-demo.com
Website: www.thornvalesecure-demo.com

(please note that the website is currently under development and not available to view)

Industry/Entity Type

Locksmith

Contact Information for Business Card

Name: Rob Kessington

Services:
Emergency Lock Out
High Security Upgrades
UPVC lock repairs
Mobile Key Cutting
Free Security Reviews

Requirements
Must have
• Ideally the cards should be a glossy black as the logo stands out better on a black background.

Logo on front and the word LOCKSMITH should be incorporated into the front design of the card.

Qualifications & Certifications on the back ideally along the top / bottom of the card or split (I.e along the top “ Accredited : Fenwick & Marrow Level 3 , TQBA”
and along the bottom , “Fully Insured & PVR Checked”

Services offered ideally listed on the back of the card, preferably split into two columns. If possible the logo could also be incorporated onto the back of the card between the two services columns (I.e the services listed either side of the logo)
Nice to have
• On the back of the card, have the logo in the middle with the services listed either side of the logo I.e 3 services on left of logo and three to the right.

```html
<!DOCTYPE html>
<html lang="en">
<head>
<meta charset="utf-8">
<title>Thornvale Secure – Business Cards</title>
<link rel="stylesheet" href="https://fonts.googleapis.com/css2?family=Cinzel:wght@500;600&family=Crimson+Text&family=Roboto:wght@400&display=swap">
<style>
  :root {
    --stage: #1d1d1f;
    --card-black: #0f0f0f;
    --card-black-soft: #1a1a1a;
    --gold-dark: #b8862a;
    --gold-mid: #e6bb52;
    --gold-light: #f6d77a;
    --ink: #1b1508;
    --white: #f2f2f2;
    --silver: #dcdcdc;
  }
  * { box-sizing: border-box; margin: 0; padding: 0; }
  html, body { width: 1200px; height: 874px; overflow: hidden; }
  body { background: var(--stage); position: relative; font-family: "Roboto", sans-serif; }

  .card {
    position: absolute;
    left: 280px;
    width: 640px;
    height: 366px;
    border-radius: 22px;
    overflow: hidden;
  }

  /* Back of card – gold */
  .card--back {
    top: 50px;
    background: linear-gradient(120deg, var(--gold-dark) 0%, var(--gold-light) 45%, var(--gold-mid) 75%, var(--gold-dark) 100%);
    color: var(--ink);
    text-align: center;
  }
  .accreditation {
    position: absolute; top: 34px; left: 0; right: 0;
    font-family: "Crimson Text", serif; font-size: 16px;
  }
  .back-brand {
    position: absolute; top: 104px; left: 0; right: 0;
    font-family: "Cinzel", serif; font-weight: 600; font-size: 36px; letter-spacing: 1px;
  }
  .services {
    position: absolute; top: 186px; left: 0; right: 0;
    list-style: none; font-size: 16px; line-height: 24px;
  }
  .services .sep {
    display: inline-block; width: 6px; height: 6px; border-radius: 50%;
    background: var(--ink); margin: 0 9px; vertical-align: middle;
  }
  .assurances {
    position: absolute; bottom: 30px; left: 0; right: 0;
    font-family: "Crimson Text", serif; font-size: 16px; letter-spacing: 0.5px;
  }

  /* Front of card – black */
  .card--front {
    top: 458px;
    background: linear-gradient(135deg, var(--card-black-soft) 0%, var(--card-black) 60%, #080808 100%);
    color: var(--white);
  }
  .front-name {
    position: absolute; left: 40px; top: 86px;
    font-family: "Cinzel", serif; font-weight: 500; font-size: 24px; color: var(--gold-mid);
  }
  .front-person { position: absolute; left: 40px; top: 120px; font-size: 17px; }
  .contacts { position: absolute; left: 40px; top: 160px; list-style: none; font-size: 16px; line-height: 23px; }
  .contacts li { display: flex; align-items: center; gap: 10px; }
  .contacts svg { width: 14px; height: 14px; fill: var(--gold-mid); flex: none; }

  .divider { position: absolute; left: 40px; top: 250px; width: 560px; height: 16px; }

  .logo-mark {
    position: absolute; right: 40px; top: 58px; width: 220px;
    text-align: center; color: var(--gold-mid);
    font-family: "Cinzel", serif; font-weight: 600; font-size: 30px; line-height: 36px;
  }
  .logo-mark .dot {
    display: block; width: 34px; height: 34px; border-radius: 50%;
    background: var(--gold-mid); margin: 0 auto 12px;
  }
  .trade {
    position: absolute; right: 96px; bottom: 34px;
    font-family: "Cinzel", serif; font-weight: 600; font-size: 19px; letter-spacing: 2px;
    color: var(--gold-mid);
  }
  .band { position: absolute; bottom: 0; height: 14px; }
  .band--gold { left: 0; width: 58%; background: linear-gradient(90deg, var(--gold-dark), var(--gold-light)); }
  .band--silver { left: 58%; right: 0; background: var(--silver); }
</style>
</head>
<body>

<section class="card card--back" aria-label="Back of business card">
  <p class="accreditation">Accredited Fenwick &amp; Marrow NVQ Level 3, TQBA</p>
  <p class="back-brand">Thornvale Secure</p>
  <ul class="services">
    <li>Emergency Lock Out<span class="sep"></span>New Lock Fitting &amp; Replacement</li>
    <li>High Security Upgrades<span class="sep"></span>UPVC lock repairs<span class="sep"></span>Mobile Key Cutting</li>
    <li>Free Security Reviews</li>
  </ul>
  <p class="assurances">FULLY INSURED • PVR CHECKED</p>
</section>

<section class="card card--front" aria-label="Front of business card">
  <p class="front-name">THORNVALE SECURE</p>
  <p class="front-person">Rob Kessington</p>
  <ul class="contacts">
    <li>
      <svg viewBox="0 0 24 24"><path d="M6.6 10.8a15.1 15.1 0 0 0 6.6 6.6l2.2-2.2c.3-.3.7-.4 1-.2 1.1.4 2.3.6 3.6.6.6 0 1 .4 1 1V20c0 .6-.4 1-1 1A17 17 0 0 1 3 4c0-.6.4-1 1-1h3.5c.6 0 1 .4 1 1 0 1.3.2 2.5.6 3.6.1.3 0 .7-.2 1z"/></svg>
      01632 960481
    </li>
    <li>
      <svg viewBox="0 0 24 24"><path d="M7 1h10a2 2 0 0 1 2 2v18a2 2 0 0 1-2 2H7a2 2 0 0 1-2-2V3a2 2 0 0 1 2-2zm0 3v14h10V4z"/></svg>
      07700900417
    </li>
    <li>
      <svg viewBox="0 0 24 24"><path d="M2 5h20v14H2zm2 2v.5l8 5 8-5V7zm0 3v7h16v-7l-8 5z"/></svg>
      contact@thornvalesecure-demo.com
    </li>
  </ul>

  <svg class="divider" viewBox="0 0 560 16" aria-hidden="true">
    <line x1="0" y1="8" x2="470" y2="8" stroke="#e6bb52" stroke-width="1"/>
    <line x1="530" y1="8" x2="560" y2="8" stroke="#e6bb52" stroke-width="1"/>
    <g fill="#e6bb52">
      <polygon points="480,3 481.8,7 486,7.3 482.8,10 483.8,14 480,11.8 476.2,14 477.2,10 474,7.3 478.2,7"/>
      <polygon points="500,3 501.8,7 506,7.3 502.8,10 503.8,14 500,11.8 496.2,14 497.2,10 494,7.3 498.2,7"/>
      <polygon points="520,3 521.8,7 526,7.3 522.8,10 523.8,14 520,11.8 516.2,14 517.2,10 514,7.3 518.2,7"/>
    </g>
  </svg>

  <div class="logo-mark"><span class="dot"></span>Thornvale<br>Secure</div>
  <p class="trade">LOCKSMITH</p>
  <div class="band band--gold"></div>
  <div class="band band--silver"></div>
</section>

</body>
</html>
```